Veltrix Website

We need a website for a new Telecommunications company based in Australia. Our service is offered to people who are in the middle of moving properties as our major channel partners relocate renters and home owners. The website will outline the products we sell, which will include pricing as well as provide information for people who are in the middle of a move. Our client base will not come from any demographic, however 95% will be people renting properties and therefore most likely range in age from 18 and upwards. I would like to have an energetic feel to the website with a young theme. It needs full integration with Social Media, must be mobile centric as well, must include video as well as have chat options for visitors and be as interactive as possible . It should not be too cluttered as it needs to be clean and feel fresh. People who are moving are time poor and stressed (I am sure you have all moved!) and therefore our service needs to be complimentary and simple for them to engage with. We have a channel passing hot leads for this purpose, however we would like to market our services to others outside of this channel. We are offering most services such as home phone, internet and prepaid mobiles as unlimited services to make things simple and easy to commit to. Logo at this stage is Red, however we also need soothing colours on the site. I like the website layout of Plovara.com as an example, as it is clean and delivers the type of feel we are after. Your design does not have to mimic it, it just needs to give off the same feel.
Updates

Specific Competitors websites include the following:

http://www.brindlepath.com.au/
http://www.quarvelink.com.au/index.asp
http://morbanwire.com.au/
http://www.feltragrid.com.au/

Our site needs to be far more interactive than these.  Chat prompts once someone is on the site would be useful - asking "Are you ready to move?" "Do you want everything unlimited?" - click to chat, etc.

Hi Designers,

Could you please look at making the designs more Telecommunications focused.  Our primary focus is to move peoples phone services, so the Telco component and Broadband and internet is a key component.  The moving information is good, however none of the designs addresses the Telecommunications part, I want it clear that when someone comes to the site they can get a new fixed line, internet and pre paid mobile phone plan.

Thanks

Gus

Target Market(s)

People moving property who want to get their telecommunication and internet services connected at their new place.

Industry/Entity Type

Internet

Requirements
Must have
• Social Media
Video section
How to section
Pricing section
Moving information section
Useful links section
Live chat

```html
<!DOCTYPE html>
<html lang="en">
<head>
<meta charset="utf-8">
<title>Veltrix – Telco for people on the move</title>
<link href="https://fonts.googleapis.com/css2?family=Open+Sans:wght@400;600;700&family=PT+Sans+Narrow:wght@400;700&family=Tinos:ital@1&display=swap" rel="stylesheet">
<style>
  :root {
    --brand-red: #e3262b;
    --brand-red-dark: #c81d22;
    --page-bg: #f0f0f0;
    --panel-bg: #e8e8e8;
    --panel-border: #d4d4d4;
    --ink: #333333;
    --ink-soft: #666666;
    --nav-active: #4a4a4a;
    --footer-bg: #4a4a4b;
    --footer-ink: #c9c9c9;
    --button-light: #ececec;
    --button-dark: #444444;
  }
  * { box-sizing: border-box; margin: 0; padding: 0; }
  html, body { width: 897px; height: 1200px; overflow: hidden; }
  body {
    position: relative;
    background: var(--page-bg);
    font-family: "Open Sans", Arial, sans-serif;
    color: var(--ink);
  }
  .abs { position: absolute; }

  /* Header */
  .top-rule { left: 0; top: 0; width: 897px; height: 3px; background: #8a8a8a; }
  .utility-links {
    left: 512px; top: 4px; width: 164px; height: 23px;
    background: #e4e4e4; border-radius: 0 0 0 12px;
    font-size: 10px; color: var(--ink-soft);
    display: flex; align-items: center; justify-content: center; gap: 5px;
  }
  .recharge {
    left: 676px; top: 3px; width: 135px; height: 29px;
    background: var(--brand-red); color: #fff;
    font-weight: 700; font-size: 12.5px;
    display: flex; align-items: center; justify-content: center;
    border-radius: 0 0 3px 3px;
  }
  .brand {
    left: 366px; top: 36px; width: 160px; height: 60px;
    display: flex; align-items: center; justify-content: center; gap: 8px;
  }
  .brand-dot { width: 18px; height: 18px; border-radius: 50%; background: var(--brand-red); }
  .brand-name { font-size: 34px; font-weight: 700; color: var(--brand-red); letter-spacing: -0.5px; }
  .brand-url { left: 366px; top: 108px; width: 160px; text-align: center; font-size: 7px; color: #777; }
  .social { left: 657px; top: 79px; display: flex; gap: 9px; }
  .social span {
    width: 23px; height: 23px; border-radius: 5px; background: #dcdcdc;
    border: 1px solid #cfcfcf; display: block;
  }

  /* Navigation */
  .nav {
    left: 79px; top: 134px; width: 732px; height: 28px;
    background: #f5f5f5; border: 1px solid var(--panel-border);
    display: flex; align-items: center; font-size: 12px; color: var(--ink);
  }
  .nav-item { height: 100%; display: flex; align-items: center; justify-content: center; border-right: 1px solid var(--panel-border); }
  .nav-item.is-active {
    background: var(--nav-active); color: #fff; height: 34px; margin-top: -6px; align-self: flex-start;
  }
  .search {
    left: 663px; top: 138px; width: 143px; height: 21px;
    background: #fff; border: 1px solid #cfcfcf;
    font-size: 8.5px; color: #999; padding-left: 7px; display: flex; align-items: center;
  }
  .search-btn { right: -1px; top: -1px; width: 21px; height: 21px; background: var(--nav-active); }

  /* Hero */
  .hero { left: 79px; top: 173px; width: 732px; height: 306px; background: var(--panel-bg); border: 1px solid var(--panel-border); }
  .hero-photo {
    left: 94px; top: 190px; width: 471px; height: 275px; border: 1px solid #cfcfcf;
    background: linear-gradient(160deg, #f4f1ec 0%, #d9b98d 45%, #c9925a 75%, #b98958 100%);
  }
  .prompt {
    left: 574px; width: 224px; background: #efefef; border: 1px solid var(--panel-border);
    padding: 9px 0 0 21px;
  }
  .prompt h3 { font-family: "PT Sans Narrow", sans-serif; font-weight: 700; font-size: 17px; color: var(--ink); line-height: 1.2; }
  .prompt p { font-size: 8.5px; color: var(--ink-soft); margin-top: 3px; }
  .prompt .chip {
    display: inline-block; margin-top: 9px; padding: 4px 7px; font-size: 8.5px; font-weight: 700;
    background: var(--button-light); border: 1px solid #c8c8c8; border-radius: 2px; color: var(--ink);
  }
  .prompt.is-featured { background: var(--brand-red); border-color: var(--brand-red-dark); }
  .prompt.is-featured h3, .prompt.is-featured p { color: #fff; }
  .prompt.is-featured .chip { background: var(--button-dark); color: #fff; border-color: #333; }

  /* Service cards */
  .service { top: 488px; width: 239px; height: 269px; background: var(--panel-bg); border: 1px solid var(--panel-border); padding: 29px 0 0 24px; }
  .service h2 { font-size: 21px; font-weight: 700; color: var(--ink); letter-spacing: 0.2px; }
  .service-step { display: flex; align-items: center; gap: 6px; margin-top: 23px; margin-left: -2px; }
  .step-num {
    width: 33px; height: 33px; border-radius: 50%; background: var(--brand-red); border: 2px solid #fff;
    box-shadow: 0 0 0 1px #d6d6d6; color: #fff; font-weight: 700; font-size: 20px;
    display: flex; align-items: center; justify-content: center;
  }
  .step-title { font-size: 13.5px; font-weight: 600; color: var(--ink); line-height: 1.1; }
  .step-sub { font-size: 8.5px; font-weight: 700; color: var(--ink); }
  .service p.body { font-size: 9.5px; line-height: 13.5px; color: var(--ink-soft); width: 194px; margin-top: 19px; text-align: justify; }
  .more {
    margin-top: 22px; width: 66px; height: 27px; font-size: 12px; font-weight: 700;
    display: flex; align-items: center; justify-content: center; border-radius: 2px;
    background: var(--button-light); border: 1px solid #c5c5c5; color: #555;
  }
  .more.is-active { background: var(--button-dark); color: #fff; border-color: #333; }

  /* Welcome */
  .welcome-title { left: 79px; top: 795px; font-size: 23px; font-weight: 700; color: var(--ink); }
  .welcome-photo {
    left: 79px; top: 843px; width: 238px; height: 132px; border: 3px solid #fff; outline: 1px solid #d0d0d0;
    background: linear-gradient(180deg, #5d8ed6 0%, #a7c4ea 45%, #6f9b45 70%, #4c7a2e 100%);
  }
  .welcome-copy { left: 342px; top: 837px; width: 208px; font-size: 8.6px; line-height: 13px; color: var(--ink-soft); text-align: justify; }
  .welcome-copy p + p { margin-top: 7px; }
  .video { left: 577px; top: 802px; width: 234px; height: 177px; background: #111; }
  .video-frame {
    left: 9px; top: 9px; width: 216px; height: 145px;
    background: radial-gradient(circle at 40% 50%, #b07a52 0%, #7d6a62 40%, #5a6f85 100%);
  }
  .play { left: 100px; top: 64px; width: 30px; height: 30px; border-radius: 50%; background: #fff; }
  .video-bar { left: 0; bottom: 0; width: 234px; height: 14px; background: linear-gradient(#8a8a8a, #5c5c5c); }

  /* Promotion */
  .promo { left: 79px; top: 1003px; width: 732px; height: 67px; background: #ebebeb; border: 1px solid var(--panel-border); outline: 2px solid #f7f7f7; outline-offset: -3px; }
  .promo-text { left: 107px; top: 1019px; font-family: "Tinos", serif; font-style: italic; font-size: 23px; color: #555; }
  .promo-btn {
    left: 689px; top: 1022px; width: 94px; height: 28px; background: var(--brand-red); color: #fff;
    font-family: "PT Sans Narrow", sans-serif; font-weight: 700; font-size: 13.5px;
    display: flex; align-items: center; justify-content: center; border-radius: 2px;
  }

  /* Footer */
  .footer { left: 0; top: 1144px; width: 897px; height: 56px; background: var(--footer-bg); }
  .footer p { position: absolute; left: 79px; top: 17px; font-size: 10px; color: var(--footer-ink); }
</style>
</head>
<body>
  <header>
    <div class="abs top-rule"></div>
    <nav class="abs utility-links"><span>Login</span>|<span>Register</span>|<span>Contact Us</span></nav>
    <a class="abs recharge">Recharge my Mobile</a>
    <div class="abs brand"><span class="brand-dot"></span><span class="brand-name">Veltrix</span></div>
    <div class="abs brand-url">www.veltrix.com.au</div>
    <div class="abs social" aria-label="Social media links"><span></span><span></span><span></span><span></span><span></span></div>
  </header>

  <nav class="abs nav">
    <div class="nav-item is-active" style="width:64px">Home</div>
    <div class="nav-item" style="width:74px">About Us</div>
    <div class="nav-item" style="width:89px">How To</div>
    <div class="nav-item" style="width:78px">Pricing</div>
    <div class="nav-item" style="width:119px">Moving Information</div>
    <div class="nav-item" style="width:84px">Useful Links</div>
    <div class="nav-item" style="width:64px">Contact</div>
  </nav>
  <div class="abs search">Search...
    <svg class="abs search-btn" viewBox="0 0 21 21"><rect width="21" height="21" fill="#4a4a4a"/><circle cx="9" cy="9" r="4.5" fill="none" stroke="#fff" stroke-width="1.8"/><line x1="12.3" y1="12.3" x2="16" y2="16" stroke="#fff" stroke-width="2"/></svg>
  </div>

  <section class="abs hero"></section>
  <div class="abs hero-photo" role="img" aria-label="Smiling family sitting among moving boxes with mobile phones and a laptop"></div>
  <div class="abs prompt is-featured" style="top:189px;height:86px">
    <h3>Are you ready to Move?</h3><p>Est omnis dolore sereled usempqu.</p><span class="chip">Click Here</span>
  </div>
  <div class="abs prompt" style="top:282px;height:89px">
    <h3>Want Everything Unlimited?</h3><p>Est omnis dolore sereled usempqu.</p><span class="chip">Click Here</span>
  </div>
  <div class="abs prompt" style="top:375px;height:90px">
    <h3>Chat with our Expert</h3><p>Est omnis dolore sereled usempqu.</p><span class="chip">Click Here</span>
  </div>

  <section class="abs service" style="left:79px">
    <h2>New Fixed Line</h2>
    <div class="service-step"><span class="step-num">1</span><div><div class="step-title">Lorem ipsum dolor sit</div><div class="step-sub">amet,consectetuadipising elit.</div></div></div>
    <p class="body">Lorem ipsum doloramet, consect etuad ipising elitsed dodesum eiusmod tempor incididunt ut laboret dolores magna aliqua.</p>
    <div class="more is-active">More</div>
  </section>
  <section class="abs service" style="left:327px">
    <h2>Internet</h2>
    <div class="service-step"><span class="step-num">2</span><div><div class="step-title">Lorem ipsum dolor sit</div><div class="step-sub">amet,consectetuadipising elit.</div></div></div>
    <p class="body">Lorem ipsum doloramet, consect etuad ipising elitsed dodesum eiusmod tempor incididunt ut laboret dolores magna aliqua.</p>
    <div class="more">More</div>
  </section>
  <section class="abs service" style="left:574px">
    <h2>Prepaid Mobile</h2>
    <div class="service-step"><span class="step-num">3</span><div><div class="step-title">Lorem ipsum dolor sit</div><div class="step-sub">amet,consectetuadipising elit.</div></div></div>
    <p class="body">Lorem ipsum doloramet, consect etuad ipising elitsed dodesum eiusmod tempor incididunt ut laboret dolores magna aliqua.</p>
    <div class="more">More</div>
  </section>

  <h2 class="abs welcome-title">Welcome Guest!</h2>
  <div class="abs welcome-photo" role="img" aria-label="Family running hand in hand across a sunny lawn"></div>
  <div class="abs welcome-copy">
    <p>Emet,consectetuadipising elit, sed dodesum eiusmod tempor incididunt ut laboret dolores magna aliqua. Ut enim ad minim veniamquis nostrud exercitation. ullamco laboris nisi ut aliquip. nulla pariatur. Excepteur sint occaecat.</p>
    <p>Ex ea commodo consequat. Duis aute irure dolor in reprehenderit in voluptate velit esse cillum dolore eu fugiat nulla pariatur. Excepteur sint occaecat cupidatat non proide sunt in culpa qui officia deserunt mollit anim id est laborum et el.</p>
  </div>
  <div class="abs video">
    <div class="abs video-frame" role="img" aria-label="Video still of a support agent wearing a headset"></div>
    <svg class="abs play" viewBox="0 0 30 30"><circle cx="15" cy="15" r="15" fill="#fff"/><path d="M12 9 L21 15 L12 21 Z" fill="#111"/></svg>
    <svg class="abs video-bar" viewBox="0 0 234 14">
      <rect x="4" y="4" width="2" height="6" fill="#eee"/><rect x="8" y="4" width="2" height="6" fill="#eee"/>
      <rect x="40" y="6" width="100" height="2" fill="#222"/><circle cx="40" cy="7" r="3" fill="#ddd"/>
      <rect x="145" y="3" width="30" height="8" fill="#222"/>
      <rect x="182" y="6" width="24" height="2" fill="#ddd"/>
      <rect x="212" y="4" width="8" height="6" fill="#ccc"/><rect x="223" y="4" width="8" height="6" fill="#ccc"/>
    </svg>
  </div>

  <section class="abs promo"></section>
  <p class="abs promo-text">Promotion lorem ipsum doloramet, consect etuad ipising</p>
  <a class="abs promo-btn">CLICK HERE</a>

  <footer class="abs footer"><p>Copyright © 2012 veltrix.com.au &nbsp;All rights reserved.</p></footer>
</body>
</html>
```